Hip-Hop Artist Rex Tamber new album cover design for "Hollow Meridian"

Artist: Rex Tamber
Album Title: Hollow Meridian
I am attaching a un-edited picture to use & some sample images with the "Hollow Meridian" concept directions. I am hoping that the graphic designers accepting this challenge can do a better or different job than the 3 sample design images attached. I do like each of the 3 attached drafts(Draft, Draft2, Draft3) concepts. But, would like to see other creative design approaches and other possible affect. artwork ideas.
I am also attaching a number of random design that I also like the direction on.
Please let em know if you have any questions, and I will respond as quickly as possible.

```html
<!DOCTYPE html>
<html lang="en">
<head>
<meta charset="utf-8">
<title>Rex Tamber – Hollow Meridian</title>
<link href="https://fonts.googleapis.com/css2?family=Open+Sans:wght@300;400&display=swap" rel="stylesheet">
<style>
  :root {
    --page: #ffffff;
    --cover: #000000;
    --title-grey: #a3a3a3;
    --artist-white: #e9e9e9;
    --rule-red: #a84c4c;
    --tone-crimson: #4a0606;
    --tone-rose: #a85656;
    --tone-grey: #5e5e5e;
    --tone-light: #b8b8b8;
  }
  html, body {
    margin: 0;
    padding: 0;
    width: 1200px;
    height: 1154px;
    overflow: hidden;
    background: var(--page);
  }
  .canvas {
    position: relative;
    width: 1200px;
    height: 1154px;
    background: var(--page);
  }
  .album-cover {
    position: absolute;
    left: 76px;
    top: 50px;
    width: 1039px;
    height: 1037px;
    background: var(--cover);
    overflow: hidden;
  }
  .portrait-area {
    position: absolute;
    inset: 0;
    width: 100%;
    height: 100%;
  }
  .cover-type {
    position: absolute;
    left: 122px;
    top: 98px;
    font-family: "Open Sans", "Segoe UI", sans-serif;
    font-weight: 300;
  }
  .artist-name {
    margin: 0;
    font-size: 35px;
    letter-spacing: 0.28em;
    color: var(--artist-white);
    line-height: 1;
    text-transform: uppercase;
  }
  .title-rule {
    width: 421px;
    height: 3px;
    margin: 20px 0 14px;
    background: var(--rule-red);
  }
  .album-title {
    margin: 0;
    font-size: 70px;
    font-weight: 300;
    line-height: 1.2;
    color: var(--title-grey);
    text-transform: uppercase;
    letter-spacing: 0.01em;
  }
</style>
</head>
<body>
<div class="canvas">
  <section class="album-cover">
    <svg class="portrait-area" viewBox="0 0 1039 1037" role="img" aria-label="Posterised red, grey and black portrait of the artist in collared shirt and tie, leaning toward the viewer">
      <defs>
        <radialGradient id="portraitTone" cx="0.68" cy="0.38" r="0.75">
          <stop offset="0" stop-color="var(--tone-light)"/>
          <stop offset="0.25" stop-color="var(--tone-rose)"/>
          <stop offset="0.5" stop-color="var(--tone-crimson)"/>
          <stop offset="0.75" stop-color="var(--tone-grey)"/>
          <stop offset="1" stop-color="var(--cover)"/>
        </radialGradient>
      </defs>
      <polygon points="540,0 1039,0 1039,1037 0,1037 0,590 300,500 470,420 520,300" fill="url(#portraitTone)"/>
    </svg>
    <div class="cover-type">
      <p class="artist-name">Rex Tamber</p>
      <div class="title-rule"></div>
      <h1 class="album-title">Hollow<br>Meridian</h1>
    </div>
  </section>
</div>
</body>
</html>
```